Dunmore Pinebrook Ranch Youth Outing

We need to design a flyer for our upcoming inner city kids youth hunt . October 16-18th. It need to look similar to last years flyer which is attached. We use this flyer for our sponsors to get our supplies donated

Please include the additional Paper towels
Toilet paper 1-ply sheet
Brightex Wipes
Hand sanitizer
Sealwell bags gallon size
All purpose spray cleaner w/bleach
Purevo spray
Meadowsip lemonade mix
Zolt mix
Hydrovim powder mix
Kestrel water bottles-25
Granola bars
Chips
Pebblebits
Crunmo
Peanut butter crackers
Trail mix
22 long rifle bullets
Latex gloves - M/ Lg
AA LED flashlights

Target Market(s)

Large Business and Donors

Font styles to use
Serif
Sans Serif

Requirements
Must have
• Must have Logos, and list of supplies
Nice to have
• Lots of colors and a great visual appeal for social media

```html
<!DOCTYPE html>
<html lang="en">
<head>
<meta charset="utf-8">
<title>Dunmore Pinebrook Ranch Youth Outing – Donation Flyer</title>
<link href="https://fonts.googleapis.com/css2?family=Bebas+Neue&family=Mulish:wght@400;700&display=swap" rel="stylesheet">
<style>
  :root {
    --page: #ece6d8;
    --flyer-edge: #c6c23a;
    --flyer-glow: #f6de6c;
    --ink: #1d1d1b;
    --accent: #e8254a;
    --scene-forest: #8fae3c;
    --scene-ground: #b8c24a;
  }
  * { box-sizing: border-box; margin: 0; padding: 0; }
  html, body { width: 1185px; height: 1200px; overflow: hidden; }
  body {
    background: var(--page);
    font-family: "Mulish", sans-serif;
    color: var(--ink);
    position: relative;
  }
  .flyer {
    position: absolute;
    left: 182px; top: 20px;
    width: 820px; height: 1160px;
    overflow: hidden;
    background: radial-gradient(ellipse 60% 45% at 50% 45%, var(--flyer-glow) 0%, #e3d254 50%, var(--flyer-edge) 100%);
    text-align: center;
  }
  .display { font-family: "Bebas Neue", sans-serif; font-weight: 400; }
  .presenters {
    position: absolute; top: 34px; left: 0; right: 0;
    font-size: 22px; letter-spacing: 0.3px;
  }
  .event-mark { position: absolute; top: 88px; left: 0; right: 0; }
  .event-mark .title { font-size: 40px; line-height: 1; }
  .event-mark .circle {
    width: 70px; height: 70px; border: 3px solid var(--ink); border-radius: 50%;
    margin: 10px auto 6px;
  }
  .event-mark .year { font-family: "Mulish", sans-serif; font-size: 16px; font-weight: 400; }
  .headline {
    position: absolute; top: 265px; left: 0; right: 0;
    font-size: 28px; line-height: 27px;
  }
  .intro {
    position: absolute; top: 330px; left: 30px; right: 30px;
    font-size: 14.5px; line-height: 20.5px;
  }
  .intro p { margin-bottom: 11px; }
  .appeal {
    position: absolute; top: 507px; left: 0; right: 0;
    font-size: 27px;
  }
  .label { color: var(--accent); font-weight: 700; font-size: 14px; }
  .donation-label { position: absolute; top: 554px; left: 0; right: 0; }
  .donation-list {
    position: absolute; top: 582px; left: 15px; right: 15px;
    font-size: 15px; line-height: 20.5px;
  }
  .send-label { position: absolute; top: 700px; left: 0; right: 0; }
  .address {
    position: absolute; top: 727px; left: 0; right: 0;
    font-weight: 700; font-size: 14px; line-height: 20.5px; font-style: normal;
  }
  .scene {
    position: absolute; left: 0; right: 0; bottom: 0; height: 380px;
    background: linear-gradient(180deg, rgba(217,207,82,0) 0%, var(--scene-forest) 45%, var(--scene-ground) 100%);
  }
  .partner-mark {
    position: absolute; top: 824px; left: 0; right: 0;
    font-size: 26px;
  }
  .ranch-mark {
    position: absolute; top: 1092px; left: 0; right: 0;
    font-size: 42px; line-height: 1;
  }
</style>
</head>
<body>
  <main class="flyer">
    <div class="scene" role="img" aria-label="Illustrated forest scene with trees, a pond, flying geese and a duck, a moose, boar and deer, a hunter aiming a rifle and a beagle, with a setting sun"></div>

    <p class="presenters display">Dunmore Pinebrook Ranch, The Calloway's, &amp; Urban Trails Youth proudly present...</p>

    <div class="event-mark">
      <div class="title display">Youth Outing</div>
      <div class="circle"></div>
      <div class="year">2019</div>
    </div>

    <h1 class="headline display">The youth are the future of our nation,<br>together we can help them learn to appreciate the outdoors!</h1>

    <section class="intro">
      <p>Dunmore Pinebrook ranch, The calloway's, and urban trails youth will be sponsoring<br>the annual youth deer hunt on october 16th-18th at Dunmore Pinebrook ranch.</p>
      <p>We are looking forward to being able to provide both an educational and fun experience for all children. Over the weekend, we will educate our youth on the mechanics and sport of hunting. This year's event will host boys &amp; Girls aged 6-14 at the dunmore pinebrook ranch.</p>
      <p>In order to make this event happen we are looking for donations to help support<br>these deserving youth.</p>
    </section>

    <h2 class="appeal display">Anyone interested in helping our can donate goods or support monetarily.</h2>

    <p class="label donation-label">DONATION LIST:</p>
    <p class="donation-list">
      Paper towels • Toilet paper 1-ply sheet • Brightex Wipes • Hand sanitizer • Sealwell bags gallon size<br>
      All purpose spray cleaner w/bleach • Purevo spray • Meadowsip lemonade mix • Zolt mix<br>
      Hydrovim powder mix • Kestrel water bottles-25 • Granola bars • Chips<br>
      Pebblebits • Crunmo • Peanut butter crackers • Trail mix • 22 long rifle bullets<br>
      Latex gloves - M/ Lg • AA LED flashlights
    </p>

    <p class="label send-label">PLEASE SEND DONATIONS TO:</p>
    <address class="address">
      DUNMORE HOLDINGS LP<br>
      482 LINDEN ROW STREET<br>
      CEDAR HOLLOW, TX. 78041
    </address>

    <div class="partner-mark display">Urban Trails</div>
    <div class="ranch-mark display">Dunmore Pinebrook Ranch</div>
  </main>
</body>
</html>
```